Quillrun Couriers Web design

Take a look at our existing website(www.qlnrun.com) and design a new one, plus coding and recreate an existing logo.

```html
<!DOCTYPE html>
<html lang="en">
<head>
<meta charset="utf-8">
<title>Quillrun Couriers</title>
<link href="https://fonts.googleapis.com/css2?family=Poppins:wght@400;500;600;700&display=swap" rel="stylesheet">
<style>
:root{
  --blue:#0d57a8;
  --blue-deep:#0a3f82;
  --orange:#f2841e;
  --ink:#1c1c1c;
  --text:#444;
  --muted:#8a8a8a;
  --dark:#232a33;
  --footer:#1f2632;
  --footer-deep:#181e28;
  --light:#f2f2f2;
  --white:#fff;
}
*{margin:0;padding:0;box-sizing:border-box}
html,body{width:1200px;height:3614px;overflow:hidden}
body{position:relative;font-family:"Poppins",sans-serif;color:var(--text);background:var(--white)}
.abs{position:absolute}
.brand{font-weight:700;color:var(--blue);font-size:24px;line-height:1.05;text-transform:uppercase;letter-spacing:.5px}
.brand small{display:block;font-size:24px;font-weight:700}
.btn{position:absolute;display:flex;align-items:center;justify-content:center;border-radius:20px;color:var(--white);font-weight:600;font-size:12px;text-transform:uppercase}
/* header */
.topbar .phone{left:751px;top:16px;font-size:11px;line-height:1.3;color:var(--ink);display:flex;gap:8px;align-items:center}
.topbar .phone b{font-weight:600}
.nav{left:372px;top:56px;width:828px;height:41px;background:var(--dark);clip-path:polygon(18px 0,100% 0,100% 100%,0 100%)}
.nav-edge{left:368px;top:56px;width:24px;height:41px;background:var(--orange);clip-path:polygon(18px 0,24px 0,6px 100%,0 100%)}
.nav ul{list-style:none;display:flex;gap:33px;position:absolute;left:41px;top:13px;font-size:11.5px;color:var(--white);text-transform:uppercase}
.nav li.active{border-bottom:2px solid var(--orange);padding-bottom:5px}
/* hero */
.hero{left:0;top:98px;width:1200px;height:600px;background:linear-gradient(90deg,#f4f5f6 0%,#eceeee 45%,#dfe4e6 100%)}
.hero-photo{left:533px;top:70px;width:560px;height:530px;background:linear-gradient(120deg,#d83a34 0%,#c63030 35%,#c8a98a 60%,#7ca2d4 85%,#e9ecef 100%);border-radius:40% 40% 0 0}
.hero h1{left:163px;top:160px;font-size:41px;line-height:50px;font-weight:700;color:var(--ink)}
.hero h1 span{color:var(--orange)}
.arrow-c{width:46px;height:46px;border-radius:50%;background:#5d8bc4;display:flex;align-items:center;justify-content:center}
/* about */
.about-bar{left:163px;top:865px;width:62px;height:242px;background:var(--blue)}
.about-photo{left:210px;top:806px;width:312px;height:360px;background:linear-gradient(160deg,#eef0f2,#d9c7b5 45%,#2a2e38 85%)}
.about .eyebrow{left:580px;top:823px;font-size:14px;font-weight:600;color:var(--blue);display:flex;align-items:center;gap:10px}
.about .eyebrow i{display:block;width:26px;height:2px;background:var(--orange)}
.about h2{left:580px;top:857px;font-size:19.5px;font-weight:700;color:var(--ink)}
.about h2 span{color:var(--orange)}
.about .lead{left:580px;top:893px;width:410px;font-size:13px;line-height:20px;color:#333}
.about .body{left:580px;top:972px;width:410px;font-size:11.5px;line-height:21px;color:#555}
/* services */
.svc-label{left:435px;top:1281px;width:330px;height:58px;border:3px solid var(--blue);text-align:center}
.svc-label small{position:absolute;top:-12px;left:50%;transform:translateX(-50%);background:var(--white);padding:0 8px;color:var(--orange);font-size:15px;font-weight:500}
.svc-label h2{font-size:31px;font-weight:700;color:var(--ink);line-height:60px}
.svc-band{left:0;top:1440px;width:1200px;height:481px}
.svc-card{position:absolute;width:300px;text-align:center;color:var(--white)}
.svc-card .ring{position:absolute;left:52px;width:196px;height:196px;border-radius:50%;border:5px solid var(--orange);background:var(--white);padding:4px}
.svc-card .ring div{width:100%;height:100%;border-radius:50%}
.svc-card .badge{position:absolute;left:122px;width:56px;height:56px;border-radius:50%;background:var(--white);display:flex;align-items:center;justify-content:center;box-shadow:0 2px 6px rgba(0,0,0,.2)}
.svc-card h3{position:absolute;width:100%;font-size:17px;font-weight:600}
.svc-card p{position:absolute;left:40px;width:220px;font-size:11.5px;line-height:18px}
.svc-card .go{position:absolute;left:134px;width:32px;height:32px;border-radius:50%;background:rgba(255,255,255,.35);display:flex;align-items:center;justify-content:center}
/* process */
.process{left:0;top:1921px;width:1200px;height:397px;background:var(--light)}
.center-head{position:absolute;width:100%;text-align:center}
.center-head small{display:block;color:var(--orange);font-size:14px;font-weight:500}
.center-head h2{font-size:29px;font-weight:700;color:var(--ink)}
.step{position:absolute;top:179px;width:168px;height:102px;background:var(--white);box-shadow:0 2px 8px rgba(0,0,0,.05);text-align:center;font-size:12.5px;color:#333}
.step svg{display:block;margin:14px auto 6px}
/* testimonials */
.reviews{left:0;top:2318px;width:1200px;height:436px;background:#f8f9fb}
.quote-card{position:absolute;top:127px;width:347px;height:112px;background:var(--white);padding:22px 22px 0 60px;font-size:11.5px;line-height:20px;color:#555}
.quote-card::before{content:"\201C";position:absolute;left:20px;top:2px;font-size:52px;font-weight:700;color:var(--blue);font-family:Georgia,serif}
.quote-card::after{content:"";position:absolute;left:40px;bottom:-10px;border:10px solid transparent;border-top-color:var(--white);border-bottom:0}
.person{position:absolute;top:274px;display:flex;align-items:center;gap:14px}
.person .avatar{width:42px;height:42px;border-radius:50%;background:linear-gradient(135deg,#e8d5c4,#b89a86)}
.person b{display:block;font-size:11px;font-weight:600;color:var(--ink);text-transform:uppercase}
.person span{font-size:10.5px;color:#aaa}
.dots{position:absolute;left:585px;top:368px;display:flex;gap:5px}
.dots i{width:7px;height:7px;border-radius:50%;border:1px solid #b9c4d3}
.dots i.on{background:var(--blue);border-color:var(--blue)}
/* quote form */
.quote-photo{left:0;top:2754px;width:553px;height:450px;background:linear-gradient(110deg,#7c8f58 0%,#c6b08e 35%,#e6d6bd 55%,#7c6d61 80%,#3f4b66 100%)}
.quote-form{left:553px;top:2754px;width:647px;height:450px;background:var(--orange)}
.quote-form h2{position:absolute;left:71px;top:90px;font-size:24px;font-weight:500;color:var(--white)}
.field{position:absolute;border:1px solid rgba(255,255,255,.45);font-size:10.5px;color:var(--white);padding:9px 12px}
.send{position:absolute;left:67px;top:344px;width:344px;height:33px;background:var(--blue);color:var(--white);font-size:10px;font-weight:600;display:flex;align-items:center;justify-content:center;letter-spacing:.5px}
/* cta */
.cta{left:0;top:3204px;width:1200px;height:79px;background:var(--dark)}
.cta p{position:absolute;left:248px;top:28px;font-size:17px;color:var(--white)}
.cta p b{font-weight:600}
.cta .btn{left:841px;top:24px;width:137px;height:34px;border-radius:0;background:var(--blue);font-size:11px}
/* footer */
.footer{left:0;top:3283px;width:1200px;height:257px;background:var(--footer);color:#cfd5de}
.footer .brand{position:absolute;left:180px;top:54px;color:var(--white);font-size:22px}
.footer .brand small{font-size:22px}
.footer .about-txt{position:absolute;left:180px;top:140px;width:200px;font-size:10px;line-height:16px}
.footer .vline{position:absolute;top:48px;width:1px;height:186px;background:#3a4352}
.fcol{position:absolute;top:60px}
.fcol h4{font-size:15px;font-weight:500;color:var(--white);position:relative;padding-top:4px}
.fcol h4::before{content:"";position:absolute;left:0;top:-10px;width:26px;height:2px;background:var(--orange)}
.fcol ul{list-style:none;margin-top:20px;font-size:11px;line-height:21px}
.fcol .row{display:flex;gap:10px;font-size:11px;line-height:16.5px;margin-top:16px}
.social{display:flex;gap:6px;margin-top:16px}
.social i{width:22px;height:22px;border-radius:50%;background:var(--blue);display:block}
.news{display:flex;margin-top:22px}
.news span{width:120px;height:26px;background:var(--white);font-size:9px;color:#999;padding:7px 10px}
.news b{width:26px;height:26px;background:var(--blue);display:flex;align-items:center;justify-content:center}
.legal{left:0;top:3540px;width:1200px;height:74px;background:var(--footer-deep);font-size:10.5px;color:#b8c0cc}
.legal span{position:absolute;top:32px}
</style>
</head>
<body>

<header class="topbar">
  <div class="abs brand" style="left:154px;top:38px">Quillrun<small>Couriers</small></div>
  <div class="abs phone">
    <svg width="22" height="22" viewBox="0 0 24 24"><path fill="#0d57a8" d="M6.6 10.8a15 15 0 0 0 6.6 6.6l2.2-2.2c.3-.3.7-.4 1-.2 1.1.4 2.3.6 3.6.6.6 0 1 .4 1 1V20c0 .6-.4 1-1 1A17 17 0 0 1 3 4c0-.6.4-1 1-1h3.5c.6 0 1 .4 1 1 0 1.3.2 2.5.6 3.6.1.3 0 .7-.2 1z"/></svg>
    <div><b>0123 456 789 10</b><br>info@qlnrun.com</div>
  </div>
  <div class="btn" style="left:926px;top:14px;width:110px;height:28px;background:var(--blue);font-size:10px">Get a Quote</div>
  <div class="abs nav-edge"></div>
  <nav class="abs nav"><ul>
    <li class="active">Home</li><li>About Us</li><li>Services</li><li>Rates</li><li>Customer Benefits</li><li>Logistics</li><li>Contact Us</li>
  </ul></nav>
</header>

<section class="abs hero">
  <div class="abs hero-photo" role="img" aria-label="Courier in red cap handing a parcel to a smiling customer who signs for it"></div>
  <h1 class="abs">PICK-UP WITHIN<br><span>15-30</span> MINUTES<br>AFTER CALL</h1>
  <div class="btn" style="left:163px;top:348px;width:165px;height:36px;background:var(--blue)">Contact Us Now</div>
  <div class="abs arrow-c" style="left:43px;top:238px"><svg width="16" height="16" viewBox="0 0 16 16"><path d="M10 2 4 8l6 6" stroke="#fff" stroke-width="2.5" fill="none"/></svg></div>
  <div class="abs arrow-c" style="left:1110px;top:238px"><svg width="16" height="16" viewBox="0 0 16 16"><path d="M6 2l6 6-6 6" stroke="#fff" stroke-width="2.5" fill="none"/></svg></div>
  <svg class="abs" style="left:589px;top:526px" width="20" height="40" viewBox="0 0 20 40"><rect x="4" y="1" width="12" height="20" rx="6" fill="none" stroke="#fff" stroke-width="1.5"/><line x1="10" y1="6" x2="10" y2="11" stroke="#fff" stroke-width="1.5"/><path d="M10 26v10M6 32l4 4 4-4" stroke="#fff" stroke-width="1.5" fill="none"/></svg>
</section>

<section class="about">
  <div class="abs about-bar"></div>
  <div class="abs about-photo" role="img" aria-label="Smiling office worker at a desk holding a cardboard parcel"></div>
  <div class="abs eyebrow"><i></i>About Us</div>
  <h2 class="abs">WELCOME TO <span>QUILLRUN COURIERS.</span></h2>
  <p class="abs lead">We are committed to providing professional messenger services to cater for the most important, emergency and time sensitive deliveries valuable to your company.</p>
  <p class="abs body">Our services range from scheduled local and long distance, same day to all types of On Demand services. Our goal is to become a leader by showing reliability, integrity as well as competitive pricing. Our company is licensed, bonded and fully insured with commercial grade insurance.</p>
  <div class="btn" style="left:580px;top:1099px;width:137px;height:35px;background:var(--orange)">Learn More</div>
</section>

<section class="services">
  <div class="abs svc-label"><small>OUR SERVICES</small><h2>WHAT WE DO</h2></div>
  <svg class="abs svc-band" width="1200" height="481" viewBox="0 0 1200 481" role="img" aria-label="Blue-tinted photo of an office meeting behind the service cards">
    <defs><linearGradient id="svcg" x1="0" y1="0" x2="1" y2="1"><stop offset="0" stop-color="#1a63b3"/><stop offset=".55" stop-color="#2f77c2"/><stop offset="1" stop-color="#0f56a6"/></linearGradient></defs>
    <path d="M0 116 Q600 -90 1200 116 V481 H0Z" fill="url(#svcg)"/>
  </svg>
  <div class="svc-card" style="left:150px;top:1413px">
    <div class="ring" style="top:0"><div role="img" aria-label="Doctor with stethoscope and digital brain scan" style="background:linear-gradient(135deg,#9fc0e6,#2a4f8a)"></div></div>
    <div class="badge" style="top:164px"><svg width="30" height="30" viewBox="0 0 24 24"><circle cx="12" cy="8" r="5" fill="none" stroke="#888" stroke-width="1.6"/><path d="M12 5.5v5M9.5 8h5" stroke="#888" stroke-width="1.6"/><path d="M3 15c3 0 5 4 9 4s6-4 9-4" stroke="#888" stroke-width="1.6" fill="none"/></svg></div>
    <h3 style="top:244px">Hospital &amp; Medical Care</h3>
    <p style="top:274px">Lorem ipsum dolor sit amet in consectetur adipiscing elit Maur in rhoncus orci pellente.</p>
    <div class="go" style="top:342px"><svg width="14" height="14" viewBox="0 0 14 14"><path d="M2 7h9M7 3l4 4-4 4" stroke="#fff" stroke-width="1.8" fill="none"/></svg></div>
  </div>
  <div class="svc-card" style="left:449px;top:1382px">
    <div class="ring" style="top:0"><div role="img" aria-label="Business partners discussing documents at a table" style="background:linear-gradient(135deg,#e8e6e2,#8a7a6a)"></div></div>
    <div class="badge" style="top:164px"><svg width="30" height="30" viewBox="0 0 24 24"><circle cx="14" cy="7" r="5" fill="none" stroke="#888" stroke-width="1.6"/><path d="M14 4.5v5" stroke="#888" stroke-width="1.4"/><path d="M2 16l4-2h6l2 2h-5M2 20h12l7-4" stroke="#888" stroke-width="1.6" fill="none"/></svg></div>
    <h3 style="top:244px">Banking &amp; Brokerage</h3>
    <p style="top:274px">Lorem ipsum dolor sit amet in consectetur adipiscing elit Maur in rhoncus orci pellente.</p>
    <div class="go" style="top:342px"><svg width="14" height="14" viewBox="0 0 14 14"><path d="M2 7h9M7 3l4 4-4 4" stroke="#fff" stroke-width="1.8" fill="none"/></svg></div>
  </div>
  <div class="svc-card" style="left:741px;top:1413px">
    <div class="ring" style="top:0"><div role="img" aria-label="Judge gavel resting on legal papers" style="background:linear-gradient(135deg,#c9ccd1,#4a4f59)"></div></div>
    <div class="badge" style="top:164px"><svg width="30" height="30" viewBox="0 0 24 24"><path d="M8 3l6 6M5 6l6 6M6.5 4.5l6 6M11 8l8 8" stroke="#888" stroke-width="2" fill="none"/><path d="M3 20h10" stroke="#888" stroke-width="2"/></svg></div>
    <h3 style="top:244px">Legal Filings</h3>
    <p style="top:274px">Lorem ipsum dolor sit amet in consectetur adipiscing elit Maur in rhoncus orci pellente.</p>
    <div class="go" style="top:342px"><svg width="14" height="14" viewBox="0 0 14 14"><path d="M2 7h9M7 3l4 4-4 4" stroke="#fff" stroke-width="1.8" fill="none"/></svg></div>
  </div>
  <div class="btn" style="left:530px;top:1808px;width:138px;height:36px;background:var(--orange)">All Services</div>
</section>

<section class="abs process">
  <div class="center-head" style="top:55px"><small>OUR WORK PROCESS</small><h2>HOW WE WORK</h2></div>
  <div class="abs" style="left:577px;top:125px;width:46px;height:2px;background:var(--orange)"></div>
  <svg class="abs" style="left:0;top:0" width="1200" height="397">
    <g fill="none" stroke="#f2841e" stroke-width="1.3" stroke-dasharray="4 4">
      <path d="M330 160 Q390 110 445 160"/><path d="M755 160 Q815 110 868 160"/><path d="M545 300 Q600 345 655 300"/>
    </g>
  </svg>
  <div class="step" style="left:194px"><svg width="40" height="44" viewBox="0 0 24 26"><path d="M6 3l3 5-2 2c1 3 3 5 6 6l2-2 5 3-2 4C10 20 4 13 3 6z" fill="#0d57a8"/><path d="M14 22c3 0 4-2 7-2" stroke="#f2841e" stroke-width="1.5" fill="none"/></svg>Request a Call</div>
  <div class="step" style="left:413px"><svg width="66" height="44" viewBox="0 0 36 24"><rect x="4" y="4" width="20" height="13" fill="#f2841e"/><path d="M24 8h6l4 5v4H24z" fill="#0d57a8"/><circle cx="10" cy="19" r="3" fill="#0d57a8"/><circle cx="29" cy="19" r="3" fill="#0d57a8"/><circle cx="14" cy="10" r="4" fill="#fff"/><path d="M14 8v2h2" stroke="#0d57a8" fill="none"/></svg>Pick-up Goods</div>
  <div class="step" style="left:623px"><svg width="46" height="44" viewBox="0 0 26 24"><path d="M4 6l3 9h8l3 5" stroke="#0d57a8" stroke-width="2.2" fill="none"/><circle cx="8" cy="4" r="2.5" fill="#0d57a8"/><path d="M7 10h6" stroke="#0d57a8" stroke-width="2.2"/><circle cx="20" cy="6" r="4" fill="none" stroke="#f2841e" stroke-width="1.5"/><path d="M20 4v2h2" stroke="#f2841e"/></svg>WAIT</div>
  <div class="step" style="left:836px"><svg width="40" height="44" viewBox="0 0 24 26"><rect x="8" y="2" width="12" height="11" fill="#f2841e"/><path d="M14 2v11" stroke="#fff"/><path d="M2 16h4l4 3h6l5-3v4l-6 4H9l-3-2H2z" fill="#0d57a8"/></svg>Deliver Your Product</div>
</section>

<section class="abs reviews">
  <div class="center-head" style="top:52px"><h2>WHAT CLIENT SAY</h2></div>
  <div class="quote-card" style="left:236px">The heights by great men reached kept attaine by sudden flight, but the while companion slept were tooiling upward in the night.</div>
  <div class="quote-card" style="left:619px">The heights by great men reached kept attaine by sudden flight, but the while companion slept were tooiling upward in the night.</div>
  <div class="person" style="left:253px"><div class="avatar" role="img" aria-label="Client portrait"></div><div><b>Mara Holt</b><span>Senior UI/UX Designer</span></div></div>
  <div class="person" style="left:636px"><div class="avatar" role="img" aria-label="Client portrait"></div><div><b>Dev Raines</b><span>Senior UI/UX Designer</span></div></div>
  <div class="dots"><i class="on"></i><i></i><i></i></div>
</section>

<section>
  <div class="abs quote-photo" role="img" aria-label="Smiling courier holding a parcel while a customer signs a clipboard at the door"></div>
  <div class="abs quote-form">
    <h2>Request A Quote</h2>
    <div class="field" style="left:69px;top:157px;width:154px;height:32px">Your Name</div>
    <div class="field" style="left:241px;top:157px;width:172px;height:32px">Your Email</div>
    <div class="field" style="left:69px;top:205px;width:344px;height:31px">Subject</div>
    <div class="field" style="left:69px;top:249px;width:344px;height:81px">Your Message</div>
    <div class="send">SEND REQUEST</div>
  </div>
</section>

<section class="abs cta">
  <p>Have any question or <b>need any business consultation?</b></p>
  <div class="btn">Contact Us Now!!</div>
</section>

<footer class="abs footer">
  <div class="brand">Quillrun<small>Couriers</small></div>
  <p class="about-txt">Lorem ipsum dolor sit amet, consectetur adipiscing elit. Nullam sollicitudin tempor sem vitae pretium. Fusce ultricies mollis purus non rutrum.</p>
  <div class="vline" style="left:393px"></div>
  <div class="vline" style="left:561px"></div>
  <div class="vline" style="left:814px"></div>
  <div class="fcol" style="left:446px"><h4>Site Links</h4><ul><li>Home</li><li>About Us</li><li>Services</li><li>Rates</li><li>Contact Us</li></ul></div>
  <div class="fcol" style="left:603px;width:200px"><h4>Contact Us</h4>
    <div class="row"><svg width="14" height="14" viewBox="0 0 24 24"><path d="M6.6 10.8a15 15 0 0 0 6.6 6.6l2.2-2.2 4.6 1.6V20A17 17 0 0 1 3 4h3.5l1.6 4.6z" fill="none" stroke="#cfd5de" stroke-width="1.6"/></svg>Phone: 123 456 78901</div>
    <div class="row"><svg width="14" height="14" viewBox="0 0 24 24"><path d="M12 22s7-7 7-12a7 7 0 0 0-14 0c0 5 7 12 7 12z" fill="none" stroke="#cfd5de" stroke-width="1.6"/><circle cx="12" cy="10" r="2.5" fill="none" stroke="#cfd5de" stroke-width="1.6"/></svg><span>Address: 123 Some State in<br>USA at 12th Street, 23th<br>New York, Ny</span></div>
    <div class="row"><svg width="14" height="14" viewBox="0 0 24 24"><rect x="3" y="6" width="18" height="13" fill="none" stroke="#cfd5de" stroke-width="1.6"/><path d="M3 6l9 7 9-7" fill="none" stroke="#cfd5de" stroke-width="1.6"/></svg>Email: mail@samplelink.com</div>
  </div>
  <div class="fcol" style="left:870px"><h4>Get Connected</h4>
    <div class="social"><i></i><i></i><i></i></div>
    <h4 style="margin-top:42px">Newsletter</h4>
    <div class="news"><span>Email...</span><b><svg width="12" height="12" viewBox="0 0 24 24"><path d="M2 12l20-9-7 19-3-8z" fill="#fff"/></svg></b></div>
  </div>
</footer>

<div class="abs legal">
  <span style="left:188px">@2021 Quillrun Couriers &nbsp;|&nbsp; All Rights Reserved.</span>
  <span style="left:826px">Terms &amp; Conditions &nbsp;|&nbsp; Privacy Policy</span>
</div>

</body>
</html>
```